Classic Minimalistic Business Card

Design a classic, minimalistic Business Card. Please find inspiration in the attached Classic Minimalistic examples. My information:
Name: Glen Ovamir
Company: Ovamir Capital
Logo: OC
Address: 1470 N Thornwick Rd, Suite 210 | Geneva, IL 60134
Phone: 630-555-0192
Email: glenovamir@pvt.insure
Slogan: Building Strength Through Capital

Feel free to leave out any of the information above except my name.

I have selected Double-sided, but I am also open to Single-sided

Target Market(s)

22-70. income greater than 150k/year

Industry/Entity Type

Finance

Contact Information for Business Card

See Project Description

Requirements
Must have
• Ivory or "antiqued" background similar to the reference pictures

```html
<!DOCTYPE html>
<html lang="en">
<head>
<meta charset="utf-8">
<title>Glen Ovamir – Business Card</title>
<link href="https://fonts.googleapis.com/css2?family=Kaushan+Script&family=Josefin+Sans:wght@300;700&family=Montserrat:wght@400&display=swap" rel="stylesheet">
<style>
  :root {
    --page: #ffffff;
    --ivory: #fbfdeb;
    --ink: #111111;
    --icon: #c9c9c9;
  }
  html, body {
    margin: 0;
    width: 1200px;
    height: 759px;
    overflow: hidden;
    background: var(--page);
  }
  .card {
    position: absolute;
    left: 75px;
    top: 75px;
    width: 1050px;
    height: 600px;
    background: var(--ivory);
    color: var(--ink);
  }
  .identity {
    position: absolute;
    left: 0;
    right: 0;
    top: 118px;
    text-align: center;
  }
  .person-name {
    margin: 0;
    font-family: "Kaushan Script", cursive;
    font-weight: 400;
    font-size: 82px;
    line-height: 110px;
  }
  .company-name {
    margin: -6px 0 0;
    font-family: "Josefin Sans", sans-serif;
    font-weight: 700;
    font-size: 39px;
    letter-spacing: 1.5px;
    line-height: 40px;
    text-transform: uppercase;
  }
  .slogan {
    margin: -4px 0 0;
    font-family: "Josefin Sans", sans-serif;
    font-weight: 300;
    font-size: 20px;
    line-height: 24px;
    text-transform: uppercase;
  }
  .contact-icons {
    position: absolute;
    left: 50px;
    top: 386px;
    display: flex;
    gap: 12px;
  }
  .contact-lines {
    position: absolute;
    left: 50px;
    top: 490px;
    font-family: "Montserrat", sans-serif;
    font-size: 28px;
    line-height: 34px;
    letter-spacing: 0.5px;
  }
  .location-icon {
    position: absolute;
    left: 836px;
    top: 385px;
  }
  .address {
    position: absolute;
    left: 680px;
    width: 320px;
    top: 454px;
    margin: 0;
    font-family: "Montserrat", sans-serif;
    font-style: normal;
    font-variant: small-caps;
    font-size: 28px;
    line-height: 35px;
    letter-spacing: 0.8px;
    text-align: center;
  }
  .address span { display: block; }
  .icon { fill: var(--icon); }
</style>
</head>
<body>
  <main class="card">
    <header class="identity">
      <h1 class="person-name">Glen Ovamir</h1>
      <p class="company-name">Ovamir Capital</p>
      <p class="slogan">Building Strength Through Capital</p>
    </header>

    <div class="contact-icons" aria-hidden="true">
      <svg class="icon phone-icon" width="54" height="56" viewBox="0 0 54 56">
        <path d="M10 4c3-2 6-1 8 2l5 9c1 3 0 5-2 7l-3 2c2 6 7 12 13 15l3-3c2-2 4-2 6-1l9 5c3 2 3 5 1 8l-4 5c-3 3-8 3-13 1C20 48 6 33 2 18 0 12 2 7 6 5z"/>
        <path d="M30 4a20 20 0 0 1 20 20h-4a16 16 0 0 0-16-16z"/>
        <path d="M30 12a12 12 0 0 1 12 12h-4a8 8 0 0 0-8-8z"/>
        <path d="M30 19a5 5 0 0 1 5 5h-5z"/>
      </svg>
      <svg class="icon mail-icon" width="60" height="54" viewBox="0 0 60 54">
        <path d="M2 4h48c1 0 2 1 2 2v1L26 25 0 7V6c0-1 1-2 2-2z"/>
        <path d="M0 12l26 18 26-18v11a16 16 0 0 0-20 17H2c-1 0-2-1-2-2z"/>
        <circle cx="46" cy="40" r="12" fill="none" stroke="#c9c9c9" stroke-width="3"/>
        <circle cx="46" cy="40" r="4.5" fill="none" stroke="#c9c9c9" stroke-width="3"/>
        <path d="M50.5 36v6c0 3 5 3 5-2" fill="none" stroke="#c9c9c9" stroke-width="3"/>
      </svg>
    </div>

    <div class="contact-lines">
      <div class="phone">630-555-0192</div>
      <div class="email">glenovamir@pvt.insure</div>
    </div>

    <svg class="icon location-icon" width="36" height="56" viewBox="0 0 36 56" aria-hidden="true">
      <path d="M18 0C8 0 0 8 0 18c0 13 18 38 18 38s18-25 18-38C36 8 28 0 18 0zm0 25a7 7 0 1 1 0-14 7 7 0 0 1 0 14z"/>
    </svg>

    <address class="address">
      <span>1470 N Thornwick Rd,</span>
      <span>Suite 210 | Geneva,</span>
      <span>IL 60134</span>
    </address>
  </main>
</body>
</html>
```